Website Design - for Energy Efficiency company - large corporate feel

Hi there,
Thanks for checking out this project!
We're a UK based energy efficiency business. We arrange for energy efficient systems to be fitted in people's houses (i.e. efficient boilers, solar panels etc.) However, we do not install them ourselves as we have accredited installers who install on our behalf. Therefore the website should appeal to these businesses and have a very professional corporate feel. The final design should communicate that we are a financially safe large corporation.
Our existing website should not be used for inspiration as the style and content are very outdated (it was from a time when were installers - which we no longer are).
The new website design should use the greens from our logo, however I don't want the site saturated in this colour.
I'm really open to your chosen layout and therefore I'm not a huge fan of including links to websites I like - as I don't want to limit your own creativity. However, I would like it to look corporate (but not too boring and unimaginative).
So here's a few links to websites that I feel give a feel of financially safe / large corporate etc. Although you certainly don't have to design with this style / layout in mind:
http://www.brenholt.org.uk/advice
http://www.tavishworks.co.uk/
http://www.dqvb.org.uk/
http://www.orrinlodgeway.co.uk/
http://www.pkwynd.co.uk/ (very bad design but looks corporate)
http://www.ferrowmoor.org.uk/
http://www.tq.co.uk/ (looks corporate but too busy and boring)
http://www.quellaro.co.uk/business/index.htm
http://www.mobrevo.com/
https://www.tervold.com/en/index.html
The site is for 4 different audiences:
Consumers | Businesses | Public Sector | Installers
Therefore, it's important that there is some form of way of splitting the site up into these sections (almost like 4 websites in 1). Each section will then have the navigation menu with 7 links.
I've attached our logo (company-logo.jpg) and another logo design we have to display inline with regulations (fair-loan-logo.jpg).
Happy designing, and thank you!

```html
<!DOCTYPE html>
<html lang="en">
<head>
<meta charset="utf-8">
<title>Leafmark Energy</title>
<link href="https://fonts.googleapis.com/css2?family=Ubuntu:wght@400;500&family=Roboto:ital,wght@0,300;0,400;1,300&display=swap" rel="stylesheet">
<style>
:root{
  --green:#8dc63f;
  --green-line:#a3d35e;
  --green-dark:#6b9a2a;
  --dark:#404040;
  --text:#3a3a3a;
  --border:#d9d9d9;
  --white:#fff;
}
*{box-sizing:border-box;margin:0;padding:0}
html,body{width:978px;height:1200px;overflow:hidden;background:#fff}
body{font-family:'Roboto',sans-serif;color:var(--text)}
.page{position:relative;width:1100px;height:1350px;transform:scale(.8891);transform-origin:0 0}
.abs{position:absolute}
.callus{left:760px;top:28px;width:256px;text-align:right;font-size:15px;font-weight:300}
.callus b{font-weight:500}
.brand{left:80px;top:48px;display:flex;align-items:center;gap:8px}
.brand-dot{width:34px;height:34px;border-radius:50%;background:var(--green)}
.brand-name{font-family:'Ubuntu',sans-serif;font-size:26px;font-weight:500;color:var(--green-dark);line-height:1}
.mainnav{left:310px;top:51px;width:709px;height:43px;background:var(--green);border-radius:3px;display:flex}
.mainnav a{flex:auto;color:#fff;text-decoration:none;font-family:'Ubuntu',sans-serif;font-size:15px;display:flex;align-items:center;justify-content:center;border-left:1px solid var(--green-line)}
.mainnav a:first-child{border-left:0}
.audience{left:81px;top:105px;width:228px;height:272px;background:var(--green);border-radius:3px 0 0 3px}
.audience a{display:flex;align-items:center;height:68px;padding-left:49px;color:#fff;text-decoration:none;font-family:'Ubuntu',sans-serif;font-weight:500;font-size:16px;border-top:1px solid var(--green-line)}
.audience a:first-child{border-top:0}
.hero{left:309px;top:105px;width:711px;height:272px;border-radius:0 3px 3px 0;background:linear-gradient(180deg,#2f7fd6 0%,#6fb0ec 35%,#a8644a 55%,#6c4a3a 80%,#d9d4c8 100%)}
.hero-caption{left:591px;top:276px;width:429px;height:47px;background:rgba(245,245,245,.88);color:var(--green-dark);font-family:'Ubuntu',sans-serif;font-size:17px;display:flex;align-items:center;justify-content:center}
.cashback{left:81px;top:391px;width:939px;height:60px;background:var(--dark);border-radius:3px;overflow:hidden}
.cashback-text{position:absolute;left:0;width:799px;top:0;height:60px;display:flex;align-items:center;justify-content:center;color:#fff;font-family:'Ubuntu',sans-serif;font-weight:500;font-size:20px}
.cashback-cta{position:absolute;right:0;top:0;width:140px;height:60px;background:var(--green);color:#fff;font-family:'Ubuntu',sans-serif;font-size:14px;line-height:17px;padding:12px 0 0 25px}
.cashback-cta svg{position:absolute;right:20px;top:12px}
.card{border:1px solid var(--border);border-radius:3px;background:#fff;padding:0 30px}
.card h2{font-family:'Ubuntu',sans-serif;font-weight:400;font-size:22px;color:var(--text);display:flex;align-items:center;gap:14px;height:40px;margin-top:20px}
.card p{font-size:14px;font-weight:300;line-height:17.5px;margin-top:14px}
.btn{position:absolute;background:var(--dark);color:#fff;font-size:13px;border-radius:3px;width:85px;height:26px;display:flex;align-items:center;justify-content:center;text-decoration:none}
.quote{font-style:italic}
.badges{left:81px;top:965px;width:937px;height:73px;border:1px solid var(--border);border-radius:3px;display:flex;align-items:center;justify-content:space-around;padding:0 30px}
.badge{background:#bdbdbd;border-radius:4px}
.footer{left:80px;top:1055px;width:940px;height:265px;background:var(--dark);color:#fff;font-size:13px;font-weight:300}
.footer h3{position:absolute;font-family:'Ubuntu',sans-serif;font-weight:500;font-size:14px}
.footer .block{position:absolute;line-height:16px}
.footer .block b{font-weight:500;font-family:'Ubuntu',sans-serif}
.contact-line{position:absolute;display:flex;align-items:center;gap:6px}
.field{position:absolute;left:575px;width:325px;background:#fff;border-radius:3px;color:#aaa;font-size:13px;padding:8px 9px}
.rule{position:absolute;left:40px;top:158px;width:480px;height:1px;background:#666}
</style>
</head>
<body>
<div class="page">
  <div class="abs callus">Call us now on <b>0800 410 7721</b></div>
  <div class="abs brand"><span class="brand-dot"></span><span class="brand-name">LEAFMARK</span></div>
  <nav class="abs mainnav">
    <a href="#">Home</a><a href="#">About Us</a><a href="#">Green Deal</a><a href="#">ECO</a><a href="#">Landlords</a><a href="#">Renewables</a><a href="#">Contact Us</a>
  </nav>
  <nav class="abs audience">
    <a href="#">For Consumers</a><a href="#">For Business</a><a href="#">For Public Sector</a><a href="#">For Installers</a>
  </nav>
  <div class="abs hero" role="img" aria-label="Photo of solar panels on a tiled cottage roof under blue sky"></div>
  <div class="abs hero-caption">We supply all your Energy Efficiency Solutions</div>

  <div class="abs cashback">
    <div class="cashback-text">Claim up to a £1000 with the Green Deal Cashback Scheme</div>
    <div class="cashback-cta">click for<br>more info
      <svg width="26" height="34" viewBox="0 0 26 34"><rect x="1" y="4" width="24" height="29" rx="12" fill="#fff"/><line x1="13" y1="4" x2="13" y2="16" stroke="#8dc63f" stroke-width="2"/><line x1="1" y1="16" x2="25" y2="16" stroke="#8dc63f" stroke-width="2"/></svg>
    </div>
  </div>

  <section class="abs card" style="left:81px;top:467px;width:461px;height:231px">
    <h2><svg width="36" height="34" viewBox="0 0 36 34"><path d="M18 2 2 17h5v15h9v-9h4v9h9V17h5z" fill="#8dc63f"/></svg>Green Deal Scheme</h2>
    <p>The Green Deal gives people the opportunity to transform their homes by paying for energy efficient home improvements with the savings on their energy bills.</p>
    <p>It is available to homeowners, tenants and landlords.</p>
    <a class="btn" href="#" style="left:333px;top:177px">more info</a>
  </section>

  <section class="abs card" style="left:558px;top:467px;width:461px;height:231px">
    <h2><svg width="30" height="30" viewBox="0 0 30 30"><path d="M25 12A10 10 0 0 0 7 8" stroke="#8dc63f" stroke-width="5" fill="none"/><path d="M5 18a10 10 0 0 0 18 4" stroke="#8dc63f" stroke-width="5" fill="none"/><path d="M2 3v10h10z" fill="#8dc63f"/><path d="M28 27V17H18z" fill="#8dc63f"/></svg>Renewables</h2>
    <p>We supply most of the latest Renewable Energy Technology including:</p>
    <p>- Solar Panels<br>- Biomass Boilers<br>- Biomass Room Heaters</p>
    <a class="btn" href="#" style="left:331px;top:177px">more info</a>
  </section>

  <section class="abs card" style="left:81px;top:715px;width:461px;height:231px">
    <h2><svg width="58" height="30" viewBox="0 0 58 30"><path d="M0 22h12v-6h8v-4h6v14h-6v-4h-8v-2H0z" fill="#8dc63f"/><rect x="30" y="2" width="8" height="26" fill="#8dc63f"/><path d="M40 4h8a10 10 0 0 1 0 22h-8z" fill="#8dc63f"/><rect x="50" y="8" width="8" height="3" fill="#8dc63f"/><rect x="50" y="19" width="8" height="3" fill="#8dc63f"/></svg>Energy Company Obligation</h2>
    <p>You might be able to get help for energy-saving improvements to your home if you’re on certain benefits and own or privately rent your home.<br>You may get all or part of the cost of:</p>
    <p>- Boiler repairs or replacements<br>- Loft or cavity wall insulation</p>
    <a class="btn" href="#" style="left:330px;top:181px">more info</a>
  </section>

  <section class="abs card" style="left:558px;top:715px;width:461px;height:231px">
    <h2><svg width="40" height="34" viewBox="0 0 40 34"><path d="M2 2h24v16H12l-6 6v-6H2z" fill="#8dc63f"/><path d="M30 8h8v16h-4v6l-6-6H14v-4h16z" fill="#8dc63f"/></svg>Testimonials</h2>
    <p class="quote">“Lorem ipsum dolor sit amet, consectetuer adipiscing elit, sed diam nonummy nibh euismod tincidunt ut laoreet dolore magna aliquam erat volutpat.”</p>
    <p class="quote" style="text-align:right;margin-top:4px;padding-right:14px">Mrs. Hale, Shropshire</p>
    <a class="btn" href="#" style="left:331px;top:179px">more info</a>
  </section>

  <div class="abs badges">
    <span class="badge" style="width:90px;height:48px;border-radius:24px"></span>
    <span class="badge" style="width:110px;height:40px"></span>
    <span class="badge" style="width:56px;height:44px;border-radius:22px"></span>
    <span class="badge" style="width:44px;height:44px;border-radius:50%"></span>
    <span class="badge" style="width:40px;height:44px"></span>
    <span class="badge" style="width:125px;height:44px"></span>
    <span class="badge" style="width:34px;height:48px"></span>
  </div>

  <footer class="abs footer">
    <h3 style="left:40px;top:21px">Address</h3>
    <h3 style="left:272px;top:21px">Contact Details</h3>
    <h3 style="left:577px;top:21px">Contact Us</h3>
    <div class="block" style="left:39px;top:50px"><b>Head office</b><br>Harlow Court<br>Quarry Lane<br>Elsdon<br>Northfield<br>NF4 2QT</div>
    <div class="block" style="left:39px;top:176px"><b>Eastvale Showroom</b><br>14 Mercer Row<br>Eastvale<br>EV2 7LP</div>
    <div class="rule"></div>
    <div class="contact-line" style="left:272px;top:54px"><svg width="24" height="16" viewBox="0 0 24 16"><rect width="24" height="16" fill="#8dc63f"/><path d="M1 1l11 8 11-8" stroke="#404040" stroke-width="1.5" fill="none"/></svg>info@leafmarkenergy.co.uk</div>
    <div class="contact-line" style="left:272px;top:86px"><svg width="26" height="18" viewBox="0 0 26 18"><path d="M1 7c0-6 24-6 24 0l-5 2-2-3H8L6 9z" fill="#8dc63f"/><path d="M6 10h14l3 7H3z" fill="#8dc63f"/><circle cx="13" cy="13" r="2.5" fill="#404040"/></svg>01632 960 418</div>
    <div class="contact-line" style="left:272px;top:180px"><svg width="24" height="16" viewBox="0 0 24 16"><rect width="24" height="16" fill="#8dc63f"/><path d="M1 1l11 8 11-8" stroke="#404040" stroke-width="1.5" fill="none"/></svg>eastvale@leafmarkenergy.co.uk</div>
    <div class="contact-line" style="left:272px;top:212px"><svg width="26" height="18" viewBox="0 0 26 18"><path d="M1 7c0-6 24-6 24 0l-5 2-2-3H8L6 9z" fill="#8dc63f"/><path d="M6 10h14l3 7H3z" fill="#8dc63f"/><circle cx="13" cy="13" r="2.5" fill="#404040"/></svg>01632 960 772</div>
    <div class="field" style="top:51px;height:32px">Name</div>
    <div class="field" style="top:92px;height:32px">Email</div>
    <div class="field" style="top:133px;height:105px">Message</div>
  </footer>
</div>
</body>
</html>
```